Website Kestrel Outdoor

Hi I'm looking for a simple design for a new website. It's outdoor products mainly in category, Boat, Tarpaulin, Fishing, Golf. I have include image and text for 8 products + presentation etc. I want a simple and modern site + fast + Mobile. Wordpress. I'm going to sell through Quorvin so I don't need any WooCommerce but a buy button to Quorvin. I haven set up the Quorvin account yet. My logo i s grey and orange. My goal is to sell in Quorvin US and later EU.

```html
<!DOCTYPE html>
<html lang="en">
<head>
<meta charset="utf-8">
<title>Kestrel Outdoor</title>
<link href="https://fonts.googleapis.com/css2?family=Montserrat:wght@400;500;600;700;800&family=Roboto:wght@400;500&display=swap" rel="stylesheet">
<style>
:root{
  --orange:#f58220;
  --ink:#222222;
  --text:#555555;
  --grey:#6d6d6d;
  --light:#f0f0f0;
  --footer:#222222;
  --white:#ffffff;
}
*{margin:0;padding:0;box-sizing:border-box}
html,body{width:1200px;height:3706px;overflow:hidden}
body{position:relative;background:var(--white);font-family:Roboto,Arial,sans-serif;color:var(--ink)}
.btn{position:absolute;display:flex;align-items:center;justify-content:center;border-radius:24px;font-family:Montserrat,Arial,sans-serif;font-weight:700;font-size:15px;letter-spacing:.3px;text-decoration:none}
.btn-orange{background:var(--orange);color:var(--white)}
.btn-white{background:var(--white);color:var(--orange)}

/* header */
.site-header{position:absolute;left:0;top:0;width:1200px;height:98px;background:var(--white);z-index:3}
.nav a{position:absolute;top:44px;font-size:14px;color:var(--ink);text-decoration:none}
.nav .home-dot{position:absolute;left:100px;top:16px;width:66px;height:66px;border-radius:50%;background:#e6e6e6}
.nav .active{color:var(--orange)}
.brand-badge{position:absolute;left:510px;top:0;width:180px;height:170px;border-radius:0 0 90px 90px;background:var(--white);z-index:4;display:flex;flex-direction:column;align-items:center;justify-content:flex-end;padding-bottom:36px}
.brand-badge .mark{width:44px;height:44px;border-radius:50%;background:#5c5c5c;margin-bottom:10px}
.brand-badge .name{font-family:Montserrat,Arial,sans-serif;font-weight:800;color:var(--orange);font-size:24px;line-height:26px;text-align:center;letter-spacing:1px}

/* hero */
.hero{position:absolute;left:0;top:98px;width:1200px;height:557px;background:linear-gradient(100deg,#3f4a3a 0%,#5b6350 40%,#7a5a3e 65%,#3b3a30 100%)}
.hero-title{position:absolute;left:112px;top:150px;color:var(--white);font-family:Montserrat,Arial,sans-serif}
.hero-title .line1{font-size:52px;font-weight:500;letter-spacing:1px;line-height:64px}
.hero-title .line2{font-size:70px;font-weight:800;line-height:80px}

/* products */
.section-title{position:absolute;left:0;width:1200px;text-align:center;font-family:Montserrat,Arial,sans-serif;font-weight:700;font-size:33px}
.section-title span{color:var(--orange)}
.product{position:absolute;top:842px;width:310px;height:290px;background:var(--light)}
.product.featured{background:var(--white);box-shadow:0 2px 10px rgba(0,0,0,.2)}
.product .photo{position:absolute;left:30px;top:10px;width:250px;height:220px;background:linear-gradient(#dcdcdc,#bdbdbd);border-radius:4px}
.product .quick{position:absolute;left:22px;top:242px;width:266px;height:40px;background:var(--orange);color:var(--white);font-family:Montserrat,Arial,sans-serif;font-weight:700;font-size:15px;display:flex;align-items:center;justify-content:center}
.product-name{position:absolute;top:1150px;width:310px;text-align:center;font-family:Montserrat,Arial,sans-serif;font-size:31px;color:var(--grey);font-weight:500}
.product-price{position:absolute;top:1198px;width:310px;text-align:center;font-size:16px;font-weight:500;color:var(--orange)}
.arrow{position:absolute;width:56px;height:56px;border-radius:50%;display:flex;align-items:center;justify-content:center}
.arrow.white{background:var(--white);box-shadow:0 2px 8px rgba(0,0,0,.2)}
.arrow.orange{background:var(--orange)}

/* feature */
.feature{position:absolute;left:0;top:1301px;width:1200px;height:515px;background:linear-gradient(90deg,#e77a1e,#ef8426 55%,#f28b2e)}
.feature h2{position:absolute;left:112px;top:120px;color:var(--white);font-size:30px;font-weight:800;line-height:39px;font-family:Montserrat,Arial,sans-serif}
.feature p{position:absolute;left:112px;top:218px;width:450px;color:var(--white);font-size:15px;line-height:26px}
.feature-photo{position:absolute;left:637px;top:51px;width:398px;height:398px;border-radius:50%;background:linear-gradient(135deg,#7b7b7b,#8c6a4e 60%,#6a6a6a)}

/* fisheries */
.fish-frame{position:absolute;left:101px;top:1911px;width:437px;height:370px;border-radius:6px;background:var(--orange)}
.fish-photo{position:absolute;left:112px;top:1901px;width:436px;height:370px;border-radius:6px;background:linear-gradient(120deg,#5b6149,#8a5a36 55%,#3f4236)}
.fish-copy h2{position:absolute;left:599px;top:1898px;font-family:Montserrat,Arial,sans-serif;font-weight:700;font-size:30px;line-height:44px;color:var(--ink)}
.fish-copy p{position:absolute;left:600px;top:2006px;width:475px;font-size:15px;line-height:26px;color:var(--text)}

/* contents */
.contents{position:absolute;left:0;top:2367px;width:1200px;height:530px;background:linear-gradient(180deg,#3a3633,#2a2624 60%,#3a332d)}
.contents .title{position:absolute;left:0;top:85px;width:1200px;text-align:center;color:var(--white);font-family:Montserrat,Arial,sans-serif;font-weight:700;font-size:29px}
.contents .sub{position:absolute;left:0;top:138px;width:1200px;text-align:center;color:var(--white);font-size:15px}
.cat{position:absolute;top:199px;width:232px;height:254px;background:var(--white);text-align:center}
.cat svg{margin-top:26px}
.cat h3{font-family:Montserrat,Arial,sans-serif;font-weight:600;font-size:22px;color:var(--orange);margin-top:12px}
.cat p{font-size:15px;line-height:26px;color:#777;margin-top:10px;padding:0 16px}
.cat.active{background:var(--orange)}
.cat.active h3{color:var(--white)}
.cat.active p{color:#ffe0c4}

/* newsletter */
.news .kicker{position:absolute;left:0;top:2984px;width:1200px;text-align:center;font-family:Montserrat,Arial,sans-serif;font-size:19px}
.news .kicker span{color:var(--orange)}
.news h2{position:absolute;left:0;top:3024px;width:1200px;text-align:center;font-family:Montserrat,Arial,sans-serif;font-weight:600;font-size:30px}
.news p{position:absolute;left:0;top:3074px;width:1200px;text-align:center;font-size:15px;font-weight:400}
.news .field{position:absolute;left:286px;top:3135px;width:628px;height:52px;border:1px solid #cfcfcf;border-radius:26px;padding-left:32px;display:flex;align-items:center;font-size:15px;color:#888}

/* footer */
.site-footer{position:absolute;left:0;top:3275px;width:1200px;height:431px;background:var(--footer);color:var(--white)}
.fcol{position:absolute;top:106px}
.fcol h4{font-family:Montserrat,Arial,sans-serif;font-weight:600;font-size:19px;margin-bottom:10px}
.fcol li{list-style:none;font-size:15px;line-height:26px}
.fcontact li{display:flex;gap:14px;margin-bottom:14px;line-height:26px}
.fdivider{position:absolute;left:112px;top:319px;width:976px;height:1px;background:#3a3a3a}
.fbrand{position:absolute;left:112px;top:350px;font-family:Montserrat,Arial,sans-serif;font-weight:700;font-size:34px;color:var(--white)}
.fcopy{position:absolute;right:112px;top:367px;font-size:14px}
</style>
</head>
<body>

<header class="site-header">
  <nav class="nav">
    <span class="home-dot"></span>
    <a class="active" href="#" style="left:111px">HOME</a>
    <a href="#" style="left:197px">ABOUT US</a>
    <a href="#" style="left:311px">PRODUCT</a>
    <a href="#" style="left:799px">SERVICES</a>
    <a href="#" style="left:911px">BLOG</a>
    <a href="#" style="left:991px">CONTACT US</a>
  </nav>
</header>
<div class="brand-badge">
  <span class="mark"></span>
  <span class="name">KESTREL<br>OUTDOOR</span>
</div>

<section class="hero" role="img" aria-label="Woman in an orange jacket and cap fishing by a forest river">
  <div class="hero-title">
    <div class="line1">WELCOME TO</div>
    <div class="line2">KESTREL OUTDOOR</div>
  </div>
  <a class="btn btn-orange" style="left:112px;top:334px;width:162px;height:46px">GET STARTED</a>
</section>

<h2 class="section-title" style="top:735px">OUR <span>PRODUCT</span></h2>

<div class="arrow white" style="left:33px;top:960px"><svg width="16" height="16" viewBox="0 0 16 16"><path d="M11 2 5 8l6 6" fill="none" stroke="#f58220" stroke-width="2.5"/></svg></div>
<div class="arrow orange" style="left:1109px;top:960px"><svg width="16" height="16" viewBox="0 0 16 16"><path d="m5 2 6 6-6 6" fill="none" stroke="#fff" stroke-width="2.5"/></svg></div>

<article class="product featured" style="left:112px">
  <div class="photo" role="img" aria-label="Grey towel with orange trim on a hook"></div>
  <div class="quick">QUICK SHOP</div>
</article>
<article class="product" style="left:446px">
  <div class="photo" role="img" aria-label="Clear water weight bag for tarpaulins"></div>
</article>
<article class="product" style="left:778px">
  <div class="photo" role="img" aria-label="Clip-on nose reading glasses with lanyard"></div>
</article>
<div class="product-name" style="left:112px">Boat</div>
<div class="product-price" style="left:112px">$52.00</div>
<div class="product-name" style="left:446px">Tarpaulin</div>
<div class="product-price" style="left:446px">$42.00</div>
<div class="product-name" style="left:778px">Clip on Nose</div>
<div class="product-price" style="left:778px">$50.00</div>

<section class="feature">
  <h2>READING GLASSES -<br>SEWING ACCESSORIES</h2>
  <p>Reading glasses to help you see the eye of the needle when threading the sewing needle. Needle eyes are small but with the help of a pair of reading glasses it will be easier. The glasses are flat and fit in the sewing box. Put on the nose with just one hand.</p>
  <a class="btn btn-white" style="left:112px;top:348px;width:162px;height:48px">LEARN MORE</a>
  <div class="feature-photo" role="img" aria-label="Smiling woman wearing glasses at a sewing machine"></div>
</section>

<section class="fish">
  <div class="fish-frame"></div>
  <div class="fish-photo" role="img" aria-label="Angler in an orange jacket holding a fishing rod and net"></div>
  <div class="fish-copy">
    <h2>GLASSES WITH<br>ENLARGEMENT FOR FISHERIES</h2>
    <p>It can be difficult to see the hook and line when tying a bow tie. A badly tied fly can mean a lost dream fish. A pair of magnifying glasses can solve the problem. Reading glasses that can be hung on the vest and that you, with one hand, can put on your nose when you tie on, for example, a bow tie.</p>
    <a class="btn btn-orange" style="left:601px;top:2171px;width:161px;height:48px">LEARN MORE</a>
  </div>
</section>

<section class="contents" aria-label="Our contents">
  <div class="title">OUR CONTENTS</div>
  <div class="sub">Lorem ipsum dolor sit amet, consectetur adipiscing elit, sed do eiusmod tempor incididunt</div>
  <div class="arrow white" style="left:51px;top:308px;width:40px;height:40px"><svg width="14" height="14" viewBox="0 0 16 16"><path d="M11 2 5 8l6 6" fill="none" stroke="#f58220" stroke-width="2.5"/></svg></div>
  <div class="arrow orange" style="left:1115px;top:308px;width:40px;height:40px"><svg width="14" height="14" viewBox="0 0 16 16"><path d="m5 2 6 6-6 6" fill="none" stroke="#fff" stroke-width="2.5"/></svg></div>

  <div class="cat" style="left:112px">
    <svg width="66" height="66" viewBox="0 0 66 66" fill="none" stroke="#f58220" stroke-width="2.5"><path d="M8 42h50l-6 14H14z"/><path d="M16 42V28h34v14M24 28V18h18v10M33 6v12M4 60c6 3 10 3 16 0 6 3 10 3 16 0 6 3 10 3 16 0"/></svg>
    <h3>Boat</h3>
    <p>Lorem ipsum dolor sit amet, consectetur adipiscing elit, sed do eiusmod tempor</p>
  </div>
  <div class="cat active" style="left:360px">
    <svg width="66" height="66" viewBox="0 0 66 66" fill="none" stroke="#fff" stroke-width="2.5"><path d="M33 8 6 56h54zM33 8l12 48M22 56l11-20 11 20M2 56h62"/></svg>
    <h3>Tarpaulin</h3>
    <p>Lorem ipsum dolor sit amet, consectetur adipiscing elit, sed do eiusmod tempor</p>
  </div>
  <div class="cat" style="left:607px">
    <svg width="66" height="66" viewBox="0 0 66 66" fill="none" stroke="#f58220" stroke-width="2.5"><path d="M14 60V30c0-14 12-22 26-20M40 10c8 2 12 8 12 16M52 26v10"/><circle cx="52" cy="42" r="6"/><path d="M20 44c6-6 14-6 20 0"/></svg>
    <h3>Fishing</h3>
    <p>Lorem ipsum dolor sit amet, consectetur adipiscing elit, sed do eiusmod tempor</p>
  </div>
  <div class="cat" style="left:856px">
    <svg width="66" height="66" viewBox="0 0 66 66" fill="none" stroke="#f58220" stroke-width="2.5"><path d="M14 4l36 48M52 4 16 52M44 52h12M10 52h12"/><circle cx="33" cy="52" r="7"/></svg>
    <h3>Golf</h3>
    <p>Lorem ipsum dolor sit amet, consectetur adipiscing elit, sed do eiusmod tempor</p>
  </div>
</section>

<section class="news">
  <div class="kicker">Special <span>Offers</span> for Subscription</div>
  <h2>SIGN UP OUR NEWSLETTER</h2>
  <p>Lorem ipsum dolor sit amet, consectetur adipiscing elit, sed do.</p>
  <div class="field">Enter email</div>
  <a class="btn btn-orange" style="left:749px;top:3135px;width:165px;height:52px;border-radius:26px">SUBSCRIBE</a>
</section>

<footer class="site-footer">
  <div class="fcol" style="left:112px">
    <h4>QUICK LINKS</h4>
    <ul><li>Home</li><li>About us</li><li>Product</li><li>Services</li><li>Blog</li><li>Contact us</li></ul>
  </div>
  <div class="fcol" style="left:324px">
    <h4>CONTACT US</h4>
    <ul class="fcontact">
      <li><svg width="12" height="16" viewBox="0 0 12 16" style="margin-top:5px"><path d="M6 0a6 6 0 0 0-6 6c0 4 6 10 6 10s6-6 6-10a6 6 0 0 0-6-6z" fill="#fff"/><circle cx="6" cy="6" r="2.2" fill="#222"/></svg><span>Lorem ipsum dolor sit amet,<br>consectetur adipiscing elit</span></li>
      <li><svg width="14" height="14" viewBox="0 0 24 24" style="margin-top:6px"><path fill="#fff" d="M6.6 10.8a15 15 0 0 0 6.6 6.6l2.2-2.2c.3-.3.7-.4 1-.2 1.1.4 2.3.6 3.6.6.6 0 1 .4 1 1V20c0 .6-.4 1-1 1A17 17 0 0 1 3 4c0-.6.4-1 1-1h3.5c.6 0 1 .4 1 1 0 1.3.2 2.5.6 3.6.1.3 0 .7-.2 1z"/></svg><span>(555) 014 2290</span></li>
      <li><svg width="14" height="12" viewBox="0 0 14 12" style="margin-top:7px"><rect width="14" height="12" rx="1" fill="#fff"/><path d="M1 1l6 5 6-5" fill="none" stroke="#222" stroke-width="1.4"/></svg><span>info@kestreloutdoor.com</span></li>
    </ul>
  </div>
  <div class="fcol" style="left:633px">
    <h4>COMPANY</h4>
    <ul><li>Terms&amp;condtions</li><li>Privacy Policy</li><li>About Us</li><li>Support</li></ul>
  </div>
  <div class="fcol" style="left:904px">
    <h4>FOLLOW US</h4>
    <ul><li>Pinecast</li><li>Trailnote</li><li>Snapfield</li><li>Worklink</li><li>Circlecast</li><li>Streamly</li></ul>
  </div>
  <div class="fdivider"></div>
  <div class="fbrand">Quorvin</div>
  <div class="fcopy">©Copyrights 2021 Company Name &nbsp;| &nbsp;All Rights Reserved</div>
</footer>

</body>
</html>
```